Stationery Design Project for Brindle Co

Hi All,

We need you to design stationary for a new online financial services business. We have already got the logo designed and it is attached. If you would like it in any other formats please let me know. If you could also if possible, match the fonts in your design to that on the logo’s provided.

What we need:
- Business Card
- A4 Letter head
- A4 Folders
- PPT template (Title page and regular page)

And what ever else you want to throw in.

We are in the process of getting the web site designed, however below is a list of websites which we like which will give you an understanding of the style that we are going for.

- plumvale.example
- hobnailworks.example
- grintablet.example
- lumpwillow.example

I look forward to your seeing your design.

• Outputs:
- Documents ready to print
- Generic editable information
- Pdf copies of the documents
- Word version of letterhead

```html
<!DOCTYPE html>
<html lang="en">
<head>
<meta charset="utf-8">
<title>Tessaro Stationery Set</title>
<link href="https://fonts.googleapis.com/css2?family=PT+Sans:wght@400;700&display=swap" rel="stylesheet">
<style>
  :root {
    --cream: #f2ebbf;
    --brand-blue: #1281ab;
    --brand-orange: #f4a020;
    --paper: #ffffff;
    --ink: #1d1d1b;
    --ink-soft: #3f4a52;
    --fold-line: #c9cfd3;
    --halo: #fbd9a4;
  }
  html, body {
    margin: 0;
    padding: 0;
    width: 848px;
    height: 1200px;
    overflow: hidden;
    background: var(--cream);
  }
  .sheet-board { display: block; width: 848px; height: 1200px; }
  .backdrop { fill: var(--cream); }
  .panel-blue { fill: var(--brand-blue); }
  .panel-white { fill: var(--paper); }
  .logo-dot { fill: var(--brand-orange); }
  .halo-dot { fill: var(--halo); }
  .fold-line { stroke: var(--fold-line); stroke-width: 1; fill: none; }
  .text, .logo-name {
    font-family: "PT Sans", sans-serif;
  }
  .logo-name { font-weight: 400; }
  .logo-name.on-blue { fill: var(--paper); }
  .logo-name.on-white { fill: var(--ink-soft); }
  .person-name { fill: var(--brand-blue); font-size: 12px; }
  .person-role { fill: var(--ink); font-size: 10px; }
  .contact { fill: var(--ink); font-size: 8px; }
  .letter-text { fill: var(--ink); font-size: 5px; }
  .letter-salute { fill: var(--ink); font-size: 6.5px; }
  .footer-text { fill: var(--ink); font-size: 4.2px; }
  .footer-text.on-blue { fill: var(--paper); }
</style>
</head>
<body>
<svg class="sheet-board" viewBox="0 0 848 1200" xmlns="http://www.w3.org/2000/svg">
  <defs>
    <clipPath id="closed-folder-shape">
      <polygon points="568,615 848,695 848,758 742,1112 450,1030"/>
    </clipPath>
  </defs>

  <rect class="backdrop" x="0" y="0" width="848" height="1200"/>

  <!-- Business card backs (blue, landscape) -->
  <g class="card-back landscape">
    <rect class="panel-blue" x="33" y="40" width="272" height="158"/>
    <circle class="logo-dot" cx="171" cy="108" r="8"/>
    <text class="logo-name on-blue" x="171" y="136" font-size="16" text-anchor="middle">tessaro</text>
  </g>
  <rect class="panel-blue card-back landscape" x="86" y="218" width="282" height="161"/>

  <!-- Business card fronts (stack with curved edge) -->
  <g class="card-front stack">
    <path class="panel-white" d="M238,160 L400,160 L400,345 L238,345 C190,300 190,205 238,160 Z"/>
    <path class="panel-white" d="M232,170 L406,170 L406,355 L232,355 C184,310 184,215 232,170 Z"/>
    <path class="panel-white" d="M222,182 L410,182 L410,344 L222,344 C172,300 172,228 222,182 Z"/>
    <text class="logo-name on-white" x="354" y="331" font-size="8.5" textLength="52" lengthAdjust="spacingAndGlyphs">tessaro.example</text>
    <path class="panel-white" d="M185,195 L412,195 L412,318 L352,318 L352,344 L412,344 L412,380 L172,380 C120,330 120,240 185,195 Z"/>
    <text class="text person-name" x="248" y="278" text-anchor="middle">Name Surname</text>
    <text class="text person-role" x="244" y="292" text-anchor="middle">position</text>
    <text class="text contact" x="205" y="311">Adress No, 12345 Country</text>
    <text class="text contact" x="205" y="321">phone. 123/456789</text>
    <text class="text contact" x="205" y="331">e-mail. name@tessaro.example</text>
    <circle class="logo-dot" cx="279" cy="360" r="6"/>
    <text class="logo-name on-white" x="289" y="364" font-size="10">tessaro.example</text>
  </g>

  <!-- Business card back (blue, portrait) -->
  <g class="card-back portrait">
    <rect class="panel-blue" x="441" y="18" width="158" height="272"/>
    <circle class="logo-dot" cx="467" cy="140" r="9"/>
    <text class="logo-name on-blue" x="482" y="147" font-size="16">tessaro.example</text>
  </g>

  <!-- Business card fronts (white, portrait, fanned) -->
  <g class="card-front portrait-stack">
    <rect class="panel-white" x="645" y="25" width="175" height="275" transform="rotate(9 732 162)"/>
    <rect class="panel-white" x="640" y="30" width="175" height="275" transform="rotate(-10 727 167)"/>
    <rect class="panel-white" x="643" y="30" width="180" height="268" transform="rotate(-2 733 164)"/>
    <circle class="logo-dot" cx="772" cy="120" r="5"/>
    <circle class="logo-dot" cx="783" cy="134" r="5"/>
    <text class="text person-name" x="730" y="142" text-anchor="middle">Name Surname</text>
    <text class="text person-role" x="726" y="156" text-anchor="middle">position</text>
    <circle class="halo-dot" cx="764" cy="260" r="30" role="img" aria-label="Soft brand circle decoration"/>
    <text class="text contact" x="659" y="258">Adress No, 12345 Country</text>
    <text class="text contact" x="659" y="269">phone. 123/456789</text>
    <text class="text contact" x="659" y="279">e-mail. name@tessaro.example</text>
  </g>

  <!-- A4 folder, open (blue) -->
  <g class="folder open">
    <rect class="panel-blue" x="27" y="740" width="611" height="431"/>
    <line class="fold-line" x1="333" y1="740" x2="333" y2="1171"/>
    <circle class="logo-dot" cx="121" cy="956" r="11"/>
    <text class="logo-name on-blue" x="140" y="964" font-size="21">tessaro</text>
    <circle class="logo-dot" cx="452" cy="1133" r="6"/>
    <text class="logo-name on-blue" x="462" y="1137" font-size="10">tessaro.example</text>
    <text class="text footer-text on-blue" x="468" y="1150">Address No. 12345 Country</text>
    <text class="text footer-text on-blue" x="468" y="1156">phone: 123/456789</text>
    <text class="text footer-text on-blue" x="468" y="1162">e-mail: name@tessaro.example</text>
  </g>

  <!-- Letterheads (back sheets) -->
  <g class="letterhead back" transform="rotate(12 420 600)">
    <path class="panel-white" d="M285,400 L560,400 L560,770 C470,740 380,752 285,780 Z"/>
    <path class="panel-blue" d="M285,780 C380,752 470,740 560,770 L560,835 L285,835 Z"/>
    <circle class="logo-dot" cx="470" cy="430" r="6"/>
    <text class="logo-name on-white" x="480" y="434" font-size="10">tessaro.example</text>
  </g>
  <g class="letterhead back" transform="rotate(9 330 600)">
    <path class="panel-white" d="M180,395 L460,395 L460,770 C370,742 280,752 180,782 Z"/>
    <path class="panel-blue" d="M180,782 C280,752 370,742 460,770 L460,835 L180,835 Z"/>
    <circle class="logo-dot" cx="360" cy="440" r="6"/>
    <text class="logo-name on-white" x="370" y="444" font-size="10">tessaro.example</text>
    <text class="text letter-salute" x="400" y="665">Best regard,</text>
    <text class="text letter-salute" x="400" y="672">Name Surname</text>
  </g>

  <!-- Letterhead (front sheet) -->
  <g class="letterhead front">
    <path class="panel-white" d="M40,440 L345,440 L345,770 C250,775 150,790 35,812 Z"/>
    <path class="panel-blue" d="M35,812 C150,790 250,775 345,770 L345,840 L35,840 Z"/>
    <circle class="logo-dot" cx="238" cy="470" r="6"/>
    <text class="logo-name on-white" x="248" y="474" font-size="10">tessaro.example</text>
    <text class="text letter-salute" x="122" y="530">Nec sine te nec tecum vivere possum</text>
    <text class="text letter-text" x="58" y="578">Lorem ipsum dolor sit amet, iusto audire splendide vix te. Ex eum dicam accusam omnesque.</text>
    <text class="text letter-text" x="58" y="585">Mel ex postea officiis voluptaria, et per dolore invenire. Mel tritani philosophia eu, ea oblique</text>
    <text class="text letter-text" x="58" y="592">suscipit voluptatum eos. Mel eu potent vocibus definitionem. Vis unum bruto cu.</text>
    <text class="text letter-text" x="58" y="603">Ad alii aliquid splendide pri, in qui posse iracundia. Quo adhuc offendit ex, ius legendos accumsan</text>
    <text class="text letter-text" x="58" y="610">ea, eum cu viris everti, quodsi accusam ne usu. Sit vidit justo detracto ne.</text>
    <text class="text letter-salute" x="224" y="705">Best regard,</text>
    <text class="text letter-salute" x="224" y="713">Name Surname</text>
    <text class="text footer-text on-blue" x="98" y="832">Address No. 12345 Country | phone: 123/456789 | e-mail: name@tessaro.example</text>
  </g>

  <!-- Envelopes / inserts (white) -->
  <g class="insert-stack">
    <polygon class="panel-white" points="325,815 478,858 460,960 310,920"/>
    <polygon class="panel-white" points="200,818 470,895 455,1030 153,945"/>
  </g>

  <!-- A4 folder, closed (white with blue sweep) -->
  <g class="folder closed">
    <polygon class="panel-white" points="568,615 848,695 848,758 742,1112 450,1030"/>
    <g clip-path="url(#closed-folder-shape)">
      <path class="panel-blue" d="M455,955 C600,992 730,975 810,915 L760,1120 L440,1040 Z"/>
    </g>
    <line class="fold-line" x1="568" y1="615" x2="450" y2="1030"/>
  </g>
</svg>
</body>
</html>
```